El Molinete Postcard

Please refer to our site for inspiration - I know this is alot of info but ?

El Molinete Reception Hall
4187C Quillmont Rd, Benicia, CA 707-555-0142
www.El-Molinete.example

Located in Benicia, California, we are a new venue that can host a variety of events. We can provide an exceptional space for your next party, reception, quinceañera, birthday party, or meeting! We treat each client with respect and go out of our way to accommodate all of your needs and make your event a success. Conveniently located just off the 680/780 junction, El Molinete is located in a safe, well-lit area with a large private parking area.

The space comes prepared with everything you need to get your party started – chairs and tables with tablecloths, a well-equipped kitchen, and incredible decorations to set the perfect backdrop to your event! Rent just the Lounge for a more intimate get-together, or add the Main Hall for your large sit-down event.

Lounge – Beautiful 1,600 ft2 entry room featuring large living room with conversation sofa seating for 40+ Sound system  Pass-through bar with seating  Fully-equipped 200 ft2 kitchen with
4-burner gas stove, oven, large double sink, full-size refrigerator, 2 microwaves, and ice machine, plus lots of storage and counter space  Newly-remodeled Men’s and Women’s bathrooms

Main Hall – Spacious 24’x80’ room with seating for up to 160 people  2,000 ft2  72” round tables with chairs, each seating up to 8 guests  DJ stand and Sound system  Atmospheric lighting
_______________________________________
Pricing -
Daytime Parties
Available 8AM-2PM
4-hour minimum

Lounge and Kitchen Only
Fri - Sat - Sun : $80/hr
Mon - Thurs : $60/hr

All Areas: Lounge, Kitchen, Main Hall, and Backyard
Fri - Sat - Sun : $120/hr
Mon - Thurs : $100/hr
___________________________________________
Evening Events
Available 3PM-12AM
5-hour minimum

Lounge and Kitchen Only -
Fri - Sat - Sun : $100/hr
Mon - Thurs : $50/hr

Fri - Sat - Sun : $160/hr
Mon - Thurs : $75/hr
___________________________________________________
Looking for a different time frame, all-day rental, or other special request? Let us know!
We'd be happy to provide you with a custom quote for your event.

I am not going to mail this postcard - only a hand out I need info and pricing on back

This is a hand out - will not be mailed

Only need my text on back

• Text and pricing on back
• Vintage feel to it

```html
<!DOCTYPE html>
<html lang="en">
<head>
<meta charset="utf-8">
<title>El Molinete – Handout</title>
<link rel="stylesheet" href="https://fonts.googleapis.com/css2?family=Courgette&family=Arimo:wght@400&display=swap">
<style>
  :root{
    --cream:#ebe4da;
    --ink:#2a1510;
    --espresso:#2b0e0d;
    --wheat:#ead8bd;
    --gold:#d7b98c;
    --ring:#9a938e;
    --photo-a:#6d5443;
    --photo-b:#3a2a22;
  }
  html,body{margin:0;padding:0;overflow:hidden;background:var(--cream);}
  .handout{position:relative;width:1200px;height:934px;overflow:hidden;font-family:"Arimo",Arial,sans-serif;}
  .panel{position:absolute;top:0;height:934px;}
  .panel--front{left:0;width:601px;background:var(--cream);border-top:3px solid var(--ink);box-sizing:border-box;}
  .panel--back{left:601px;width:599px;background:var(--espresso);}
  .back-rule{position:absolute;left:0;right:0;height:3px;background:var(--wheat);}
  .back-rule--a{top:0;}
  .back-rule--b{top:7px;height:2px;}
  .front-title{position:absolute;left:0;width:590px;top:40px;margin:0;text-align:center;
    font-family:"Courgette",cursive;font-weight:400;font-size:74px;color:var(--ink);letter-spacing:1px;}
  .gallery{position:absolute;left:0;top:0;width:601px;height:934px;}
  .venue-details{position:absolute;left:23px;top:703px;width:560px;margin:0;
    font-size:12.6px;line-height:16.3px;color:var(--ink);}
  .venue-details p{margin:0 0 16.3px;}
  .back-title{position:absolute;left:0;width:599px;top:100px;margin:0;text-align:center;
    font-family:"Courgette",cursive;font-weight:400;font-size:34px;color:var(--gold);}
  .flourish{position:absolute;height:6px;border-radius:3px;background:var(--gold);opacity:.85;}
  .flourish--title-l{left:100px;top:124px;width:66px;}
  .flourish--title-r{left:421px;top:124px;width:76px;}
  .flourish--divider{left:181px;width:236px;height:8px;background:var(--wheat);}
  .flourish--one{top:449px;}
  .flourish--two{top:731px;}
  .pricing{position:absolute;left:0;width:599px;margin:0;text-align:center;
    font-size:13.4px;line-height:18.25px;color:var(--wheat);}
  .pricing p{margin:0 0 18.25px;}
  .pricing--day{top:208px;}
  .pricing--evening{top:500px;}
  .pricing--custom{top:769px;}
</style>
</head>
<body>
<main class="handout">
  <section class="panel panel--front">
    <h1 class="front-title">El Molinete</h1>

    <svg class="gallery" viewBox="0 0 601 934" aria-hidden="false">
      <defs>
        <radialGradient id="photoTone" cx="50%" cy="40%" r="70%">
          <stop offset="0" stop-color="var(--photo-a)"/>
          <stop offset="1" stop-color="var(--photo-b)"/>
        </radialGradient>
      </defs>
      <path d="M20 470 C20 300 150 250 250 270 C300 200 330 180 373 190 C430 200 470 230 540 250 C590 280 601 320 601 320"
            fill="none" stroke="var(--ink)" stroke-width="2.5"/>
      <path d="M380 700 C450 760 560 740 580 650" fill="none" stroke="var(--ink)" stroke-width="2.5"/>

      <g class="photo-frame">
        <circle cx="205" cy="464" r="196" fill="var(--cream)" stroke="var(--ink)" stroke-width="2.5"/>
        <circle cx="205" cy="464" r="189" fill="url(#photoTone)" stroke="var(--ring)" stroke-width="4"
                role="img" aria-label="Photo of the lounge with sofas, round pendant lights and tall windows"/>
      </g>
      <g class="photo-frame">
        <circle cx="373" cy="243" r="54" fill="var(--cream)" stroke="var(--ink)" stroke-width="2.5"/>
        <circle cx="373" cy="243" r="48" fill="url(#photoTone)" stroke="var(--ring)" stroke-width="3"
                role="img" aria-label="Photo of a lounge corner with an armchair and lamp"/>
      </g>
      <g class="photo-frame">
        <circle cx="502" cy="347" r="97" fill="var(--cream)" stroke="var(--ink)" stroke-width="2.5"/>
        <circle cx="502" cy="347" r="90" fill="url(#photoTone)" stroke="var(--ring)" stroke-width="3"
                role="img" aria-label="Photo of the lounge seating area by the windows"/>
      </g>
      <g class="photo-frame">
        <circle cx="472" cy="616" r="112" fill="var(--cream)" stroke="var(--ink)" stroke-width="2.5"/>
        <circle cx="472" cy="616" r="105" fill="url(#photoTone)" stroke="var(--ring)" stroke-width="3"
                role="img" aria-label="Photo of a buffet table set with food and flowers"/>
      </g>
    </svg>

    <div class="venue-details">
      <p>Lounge – Beautiful 1,600 ft2 entry room<br>
      featuring large living room with conversation<br>
      sofa seating for 40+ Sound system<br>
      Pass-through bar with seating&nbsp; Fully-equipped<br>
      200 ft2 kitchen with<br>
      4-burner gas stove, oven, large double sink, full-size<br>
      refrigerator, 2 microwaves, and ice machine, plus lots of storage and counter<br>
      space&nbsp; Newly-remodeled Men’s and Women’s bathrooms</p>
      <p>Main Hall – Spacious 24’x80’ room with seating for up to 160 people&nbsp; 2,000 ft2<br>
      72” round tables with chairs, each seating up to 8 guests&nbsp; DJ stand and Sound<br>
      system&nbsp; Atmospheric lighting.</p>
    </div>
  </section>

  <section class="panel panel--back">
    <div class="back-rule back-rule--a"></div>
    <div class="back-rule back-rule--b"></div>

    <div class="flourish flourish--title-l" role="img" aria-label="Decorative scroll flourish"></div>
    <h2 class="back-title">El Molinete</h2>
    <div class="flourish flourish--title-r" role="img" aria-label="Decorative scroll flourish"></div>

    <div class="pricing pricing--day">
      <p>Pricing -<br>Daytime Parties<br>Available 8AM-2PM<br>4-hour minimum</p>
      <p>Lounge and Kitchen Only<br>Fri - Sat - Sun : $80/hr<br>Mon - Thurs : $60/hr</p>
      <p>All Areas: Lounge, Kitchen, Main Hall, and Backyard<br>Fri - Sat - Sun : $120/hr<br>Mon - Thurs : $100/hr</p>
    </div>

    <div class="flourish flourish--divider flourish--one" role="img" aria-label="Decorative scroll divider"></div>

    <div class="pricing pricing--evening">
      <p>Evening Events<br>Available 3PM-12AM<br>5-hour minimum</p>
      <p>Lounge and Kitchen Only -<br>Fri - Sat - Sun : $100/hr<br>Mon - Thurs : $50/hr</p>
      <p>All Areas: Lounge, Kitchen, Main Hall, and Backyard<br>Fri - Sat - Sun : $160/hr<br>Mon - Thurs : $75/hr</p>
    </div>

    <div class="flourish flourish--divider flourish--two" role="img" aria-label="Decorative scroll divider"></div>

    <div class="pricing pricing--custom">
      <p>Looking for a different time frame, all-day rental,<br>or other special request? Let us know!<br>We'd be happy to provide you with a custom quote for your event.</p>
    </div>
  </section>
</main>
</body>
</html>
```